PostCard Design Project

I am making a mailing postcard
I am having the mailing printed using 4 color foil on certain parts.
I am looking for a design that maximizes the foil process where certain parts are done in foil to grab the customers attention (example: if there is a car on the postcard the headlights would be done in foil) .
I am targeting some industries, (auto, real estate, medical, beauty) I would like the post card to have examples of postcard ideas for 2 or 3 of these industries.
specs:
the postcard should be atleast 6.5x9 up to 8.5x11, I don't want to restrict the space for the creative as I don't want everything to look like a huge mess. both sides will be used.
the piece is a direct mail piece so it has to meet requirements of https://www.kelvanepost.example/business/pdf/quick-reference-guide.pdf
text will be
"business with no limits, meet mailing with no addresses, gain new customers through "Open Lane Parcel Drop" reach new customers at their home without needing their address. "
I also want some current print specials I am running included.
-double your order FREE (order 500 business cards and get 1000)
-250 100lb gloss stock brochures 99.00
-business packages (cards, envelopes and letterhead) 299
-1000 flyers 140.40
-5000 postcards 179.99
A list of services
banners
booklets
brochures
business cards
calendars
catalogs
CD/DVD packages
envelopes
event tickets
flyers
hangtags
postcards
posters
presentation folders
rack cards
labels
table tents
window cling and decal
"order 24/7 orders@quillory.example" must be included
my logo is Quillory will be supplied later
ive received some great designs. however Im looking for something a little more modern like some tavren would put out. if the amount of words is too much please feel free to edit. also an idea i had for the list of services i offer is to have it transparent yet readable as the background of the postcard some small some big but covering the entire backgroud. you can then design on top of that with other thing. just an early morning thought
Reason: I have uploaded a sketch of my idea, please take time to look at it for an accurate depiction of what im looking for. feel free to add elements that make it pop off the page
Reason: We are getting close i will be providing feed back today

```html
<!DOCTYPE html>
<html lang="en">
<head>
<meta charset="utf-8">
<title>Quillory Postcard</title>
<link href="https://fonts.googleapis.com/css2?family=Arimo:wght@400;700&family=Oswald:wght@600;700&display=swap" rel="stylesheet">
<style>
  :root {
    --backdrop: #e9ead9;
    --card: #1b1b1b;
    --yellow: #f5ea1e;
    --red: #e3232b;
    --deep-red: #c7202a;
    --orange: #f7931e;
    --gold: #f2c12e;
    --lime: #d7ef2a;
    --sky: #5ccff0;
    --tile-orange: #fba12b;
    --white: #ffffff;
    --ghost: rgba(255,255,255,0.13);
  }
  * { box-sizing: border-box; margin: 0; padding: 0; }
  html, body { width: 904px; height: 1200px; overflow: hidden; background: var(--backdrop); }
  body { position: relative; font-family: "Arimo", Arial, sans-serif; }

  .card { position: absolute; left: 95px; width: 714px; background: var(--card); overflow: hidden; }
  .card--front { top: 74px; height: 514px; }
  .card--back { top: 602px; height: 517px; }

  /* Front */
  .headline { position: absolute; left: 36px; top: 20px; color: var(--yellow); font-weight: 700; font-size: 41px; letter-spacing: 0.3px; }
  .shine { position: absolute; left: 34px; top: 72px; color: var(--deep-red); font-family: "Oswald", Impact, sans-serif; font-weight: 700; font-size: 64px; line-height: 1; }
  .hours, .email { position: absolute; left: 36px; color: var(--orange); font-family: "Oswald", Impact, sans-serif; font-weight: 700; font-size: 33px; line-height: 1; }
  .hours { top: 160px; }
  .email { top: 204px; }
  .brand { position: absolute; left: 36px; top: 253px; width: 203px; height: 63px; background: var(--white); display: flex; align-items: center; gap: 10px; padding-left: 16px; }
  .brand__mark { width: 22px; height: 22px; background: var(--orange); }
  .brand__name { font-size: 26px; color: #3b7cc4; font-weight: 400; }

  .photo { position: absolute; }
  .photo--smile-band { left: 441px; top: 126px; width: 273px; height: 12px; background: var(--orange); }
  .photo--smile { left: 441px; top: 138px; width: 273px; height: 147px; background: linear-gradient(90deg, #d98a7e, #f1e4de 50%, #d88d80); }
  .photo--car-panel { left: 380px; top: 279px; width: 16px; height: 159px; background: var(--red); }
  .photo--car { left: 396px; top: 279px; width: 246px; height: 159px; background: linear-gradient(135deg, #d8242a 0%, #8e1116 45%, #1d1d1f 70%, #444 100%); }
  .photo--portrait { left: 181px; top: 332px; width: 244px; height: 157px; background: linear-gradient(90deg, #f4f4f4, #e7c7b5 55%, #f2f2f2); }

  /* Back */
  .ghost-word { position: absolute; color: var(--ghost); font-size: 16px; white-space: nowrap; }
  .services-title { position: absolute; left: 42px; top: 40px; color: var(--white); font-size: 35px; font-weight: 400; }
  .services { position: absolute; left: 42px; top: 105px; list-style: none; }
  .services li { color: var(--white); font-size: 14.5px; line-height: 22.7px; display: flex; align-items: center; gap: 8px; }
  .services li::before { content: ""; width: 5px; height: 5px; border-radius: 50%; background: var(--dot, #fff); }
  .pitch { position: absolute; left: 221px; top: 32px; width: 300px; color: var(--white); font-size: 13px; line-height: 17px; }
  .indicia { position: absolute; left: 612px; top: 19px; width: 82px; height: 80px; background: var(--white); color: #111; font-size: 9.5px; line-height: 12px; text-align: center; padding-top: 6px; }
  .indicia strong { font-size: 12px; font-weight: 400; }
  .address { position: absolute; left: 530px; top: 118px; width: 164px; height: 79px; background: var(--white); color: #111; font-size: 13px; line-height: 16px; padding: 22px 0 0 18px; }

  .offer { position: absolute; border-radius: 14px; display: flex; align-items: center; justify-content: center; text-align: center; font-weight: 700; padding: 6px; }
  .offer--double { left: 250px; top: 167px; width: 131px; height: 96px; background: var(--lime); color: #111; font-size: 13px; line-height: 16px; }
  .offer--package { left: 250px; top: 274px; width: 131px; height: 105px; background: var(--red); color: var(--white); font-size: 12.5px; line-height: 15px; }
  .offer--brochure { left: 388px; top: 285px; width: 118px; height: 94px; background: var(--sky); color: #111; font-size: 13px; line-height: 16px; }
  .offer--flyers { left: 250px; top: 388px; width: 124px; height: 108px; background: var(--red); color: var(--white); font-size: 20px; line-height: 24px; }
  .offer--postcards { left: 381px; top: 386px; width: 111px; height: 96px; background: var(--tile-orange); color: #111; font-size: 14px; line-height: 17px; }
  .specials-label { position: absolute; left: 392px; top: 168px; color: var(--gold); font-size: 31px; font-weight: 700; line-height: 30px; }
</style>
</head>
<body>

<section class="card card--front">
  <h1 class="headline">Let Us Help Your Business</h1>
  <p class="shine">SHINE !</p>
  <p class="hours">24 hr/ 7day</p>
  <p class="email">orders@quillory.example</p>
  <div class="brand"><span class="brand__mark"></span><span class="brand__name">Quillory</span></div>

  <div class="photo photo--smile-band"></div>
  <div class="photo photo--smile" role="img" aria-label="Close-up photo of a smile with braces beside a bright white smile"></div>
  <div class="photo photo--car-panel"></div>
  <div class="photo photo--car" role="img" aria-label="Photo of a red sports car headlight"></div>
  <div class="photo photo--portrait" role="img" aria-label="Beauty portrait photo of a woman with styled hair"></div>
</section>

<section class="card card--back">
  <span class="ghost-word" style="left:285px;top:110px;transform:rotate(-8deg)">business cards</span>
  <span class="ghost-word" style="left:420px;top:110px;transform:rotate(60deg)">CD/DVD</span>
  <span class="ghost-word" style="left:460px;top:140px;transform:rotate(-70deg)">booklets</span>
  <span class="ghost-word" style="left:500px;top:100px;transform:rotate(20deg)">calendars</span>
  <span class="ghost-word" style="left:620px;top:205px;transform:rotate(12deg)">calendars</span>
  <span class="ghost-word" style="left:215px;top:220px;transform:rotate(-40deg)">envelopes</span>
  <span class="ghost-word" style="left:205px;top:290px;transform:rotate(-55deg)">flyers</span>
  <span class="ghost-word" style="left:535px;top:240px;transform:rotate(45deg)">CD/ DVD packages</span>
  <span class="ghost-word" style="left:435px;top:245px;transform:rotate(-70deg)">catalogs</span>
  <span class="ghost-word" style="left:500px;top:270px;transform:rotate(-60deg)">tickets</span>
  <span class="ghost-word" style="left:188px;top:340px;transform:rotate(-10deg)">hangtags</span>
  <span class="ghost-word" style="left:215px;top:400px;transform:rotate(-25deg)">postcards</span>
  <span class="ghost-word" style="left:545px;top:315px;transform:rotate(30deg)">rackcards</span>
  <span class="ghost-word" style="left:500px;top:420px;transform:rotate(20deg)">posters</span>
  <span class="ghost-word" style="left:505px;top:460px;transform:rotate(12deg)">presentation folders</span>
  <span class="ghost-word" style="left:460px;top:480px;transform:rotate(8deg)">labels</span>

  <h2 class="services-title">Services</h2>
  <ul class="services">
    <li style="--dot:#8bd13d">banners</li>
    <li style="--dot:#3b8de0">booklets</li>
    <li style="--dot:#2a4fb8">brochures</li>
    <li style="--dot:#e33d8f">business cards</li>
    <li style="--dot:#f2d21e">calendars</li>
    <li style="--dot:#f26a1e">catalogs</li>
    <li style="--dot:#d42a2a">CD/DVD packages</li>
    <li style="--dot:#f2891e">envelopes</li>
    <li style="--dot:#c8e12a">event tickets</li>
    <li style="--dot:#6ad23a">flyers</li>
    <li style="--dot:#2f9a4a">hangtags</li>
    <li style="--dot:#5ccff0">postcards</li>
    <li style="--dot:#1e6fd8">posters</li>
    <li style="--dot:#9b2fc2">presentation folders</li>
    <li style="--dot:#1e2fb8">rackcards</li>
    <li style="--dot:#ffffff">labels</li>
  </ul>

  <p class="pitch">Business with no limits, meet mailing with no addresses, gain new customers through "Open Lane Parcel Drop" reach new customers at their home without needing their address.</p>

  <div class="indicia">PRSRT STD<br>ECRWSS<br>U.S.POSTAGE<br><strong>PAID</strong><br>OLPD Retail</div>
  <div class="address">Local<br>Postal Customer</div>

  <div class="offer offer--double">Double your order FREE (order 500 business cards and get 1000)</div>
  <p class="specials-label">current<br>specials<br>print</p>
  <div class="offer offer--package">Business packages (cards, envelopes and letterhead) 299</div>
  <div class="offer offer--brochure">250 100lb gloss stock brochures 99.00</div>
  <div class="offer offer--flyers">1000 flyers<br>140.40</div>
  <div class="offer offer--postcards">5000 postcards 179.99</div>
</section>

</body>
</html>
```